Energy Drink Brands Packaging Design

I require design for a startup energy drink, This will be the design that will be printed on the cans.

Name
482

Brief
Must think disruptive, 482 is the beasts number so I would want the eyes of satan/devil incorporated within the design however the design must be clean, and not too busy most of the attention must be given to the name and the beasts eyes. I have attached image of a major energy drink , I would like to use a similar layout and colour scheme whilst incorporating my own branding statements
Updates

Reason: I have extended the deadline as there are some very strong designs coming through.

Target Market(s)

All energy drink lovers, males, females etc

Industry/Entity Type

Startup

Font styles to use
Sans Serif

Colors
0255a3
f3f1f8

Requirements
Must have
• Similar colour layout to the major energy Drink brand we all know KV
Nice to have
• I would like to see different concepts of a satanic/beast eyes whilst giving it a sleek and attractive look

```html
<!DOCTYPE html>
<html lang="en">
<head>
<meta charset="utf-8">
<title>482 Energy Drink Can Label</title>
<link rel="stylesheet" href="https://fonts.googleapis.com/css2?family=Jost:wght@700&display=swap">
<style>
  :root {
    --brand-blue: #0255a3;
    --brand-white: #f3f1f8;
    --stage-grey: #e4e4e6;
    --wave-blue: #1a7fcf;
    --wave-light: #8cc4ec;
    --mist-grey: #d6d7db;
  }
  * { margin: 0; padding: 0; box-sizing: border-box; }
  html, body {
    width: 1200px;
    height: 907px;
    overflow: hidden;
  }
  body {
    background: var(--stage-grey);
    position: relative;
  }
  .can-label {
    position: absolute;
    left: 381px;
    top: 0;
    width: 438px;
    height: 907px;
    overflow: hidden;
    background: var(--brand-white);
  }
  .label-backdrop {
    position: absolute;
    inset: 0;
  }
  .beast-eyes {
    position: absolute;
    left: 68px;
    top: 188px;
    width: 300px;
    height: 208px;
    border-radius: 8px;
    background: radial-gradient(ellipse at 50% 45%, #c9ccd3 0%, #9aa3b1 55%, #dfe2e8 100%);
    opacity: 0.85;
  }
  .brand-name {
    position: absolute;
    left: 40px;
    right: 40px;
    top: 432px;
    text-align: center;
    white-space: nowrap;
    font-family: "Jost", sans-serif;
    font-weight: 700;
    font-size: 196px;
    line-height: 1;
    letter-spacing: -8px;
    text-indent: -8px;
    color: var(--brand-blue);
  }
</style>
</head>
<body>
  <main class="can-label">
    <svg class="label-backdrop" width="438" height="907" viewBox="0 0 438 907" aria-hidden="true">
      <defs>
        <linearGradient id="topMist" x1="0" y1="0" x2="0" y2="1">
          <stop offset="0" stop-color="#cfd0d4"/>
          <stop offset="1" stop-color="#f3f1f8"/>
        </linearGradient>
        <linearGradient id="waveBack" x1="0" y1="0" x2="1" y2="0">
          <stop offset="0" stop-color="#dfe9f5"/>
          <stop offset="0.5" stop-color="#f3f6fb"/>
          <stop offset="1" stop-color="#b9cfe8"/>
        </linearGradient>
        <linearGradient id="waveFront" x1="0" y1="0" x2="1" y2="0">
          <stop offset="0" stop-color="#1a7fcf"/>
          <stop offset="0.45" stop-color="#8cc4ec"/>
          <stop offset="1" stop-color="#2a6fb8"/>
        </linearGradient>
      </defs>
      <rect width="438" height="907" fill="#f3f1f8"/>
      <path d="M0 0 H438 V40 C320 60 160 110 0 180 Z" fill="url(#topMist)"/>
      <path d="M0 180 C140 110 300 75 438 70 V110 C300 120 150 160 0 230 Z" fill="#e6e7ea" opacity="0.7"/>
      <path d="M0 710 C140 690 300 690 438 705 V907 H0 Z" fill="url(#waveBack)"/>
      <path d="M0 765 C150 740 300 745 438 770 V907 H0 Z" fill="url(#waveFront)"/>
    </svg>
    <div class="beast-eyes" role="img" aria-label="Illustration of a pair of fierce beast eyes with blue irises and dark striped markings"></div>
    <h1 class="brand-name">482</h1>
  </main>
</body>
</html>
```